Wall poster for our in home gym.

I would like a poster that has a unique logo or icon for our in home Gym. We want to call it "The PLOX" or "The Grand PLOX" given our last name is Fenwick. We work out with Dumbells, barbells, kettle bells, jump rope, sleds, tires, sledge hammers, pullups, pushups..etc...
The room is Half way up the wall red, the rest white with green artificial turf...
Reason: I am going to eliminate all those I dont want and then suggest some changes to those I like.
Gym

```html
<!DOCTYPE html>
<html lang="en">
<head>
<meta charset="utf-8">
<title>The Grand PLOX – Home Gym Poster</title>
<link rel="stylesheet" href="https://fonts.googleapis.com/css2?family=Arimo:ital,wght@0,700;1,400;1,700&family=Fredoka:wght@700&display=swap">
<style>
  :root {
    --night: #140604;
    --night-warm: #1e0b07;
    --skin: #c58564;
    --skin-light: #d9a07e;
    --gold: #f2c21e;
    --band-edge: #e8b51f;
    --band-mid: #f0d27a;
    --brick: #c4302b;
    --brick-deep: #9e2420;
    --ink: #1a1a1a;
  }
  html, body {
    margin: 0;
    padding: 0;
    overflow: hidden;
    background: #ffffff;
  }
  .poster {
    position: relative;
    width: 900px;
    height: 1200px;
    overflow: hidden;
    background: var(--night);
  }
  .hero-photo {
    position: absolute;
    left: 0;
    top: 0;
    width: 900px;
    height: 858px;
    background:
      radial-gradient(ellipse 62% 26% at 48% 72%, var(--skin-light) 0%, var(--skin) 60%, rgba(197,133,100,0) 100%),
      linear-gradient(180deg, var(--night) 0%, var(--night-warm) 100%);
  }
  .title-the {
    position: absolute;
    left: 58px;
    top: 272px;
    margin: 0;
    font-family: "Fredoka", sans-serif;
    font-weight: 700;
    font-size: 150px;
    line-height: 1;
    color: var(--gold);
    letter-spacing: -2px;
  }
  .title-grand {
    position: absolute;
    left: 165px;
    top: 528px;
    margin: 0;
    font-family: "Fredoka", sans-serif;
    font-weight: 700;
    font-size: 140px;
    line-height: 1;
    color: rgba(232, 170, 130, 0.6);
    text-shadow:
      -4px -4px 6px rgba(255, 220, 190, 0.45),
      6px 8px 10px rgba(90, 40, 20, 0.55);
  }
  .name-band {
    position: absolute;
    left: 0;
    top: 858px;
    width: 900px;
    height: 342px;
    background: linear-gradient(90deg, var(--band-edge) 0%, var(--band-mid) 50%, var(--band-edge) 100%);
  }
  .brand-name {
    position: absolute;
    left: 0;
    width: 850px;
    top: 14px;
    margin: 0;
    text-align: center;
    font-family: "Arimo", sans-serif;
    font-weight: 700;
    font-size: 250px;
    line-height: 1;
    letter-spacing: -6px;
    color: var(--brick);
    -webkit-text-stroke: 3px var(--gold);
    text-shadow: -10px 7px 0 var(--brick-deep);
  }
  .band-rule {
    position: absolute;
    left: 12px;
    right: 8px;
    top: 264px;
    height: 4px;
    background: var(--brick);
  }
  .tagline {
    position: absolute;
    left: 0;
    width: 856px;
    top: 288px;
    margin: 0;
    text-align: center;
    font-family: "Arimo", sans-serif;
    font-style: italic;
    font-weight: 400;
    font-size: 28px;
    color: var(--ink);
  }
  .tagline strong {
    font-weight: 700;
  }
</style>
</head>
<body>
  <main class="poster">
    <div class="hero-photo" role="img" aria-label="Photo of a flexed muscular arm against a dark background"></div>
    <p class="title-the">The</p>
    <p class="title-grand">GRAND</p>
    <section class="name-band">
      <h1 class="brand-name">PLOX</h1>
      <div class="band-rule"></div>
      <p class="tagline">building ‘<strong>FENWICK</strong>’ muscles</p>
    </section>
  </main>
</body>
</html>
```